Letterhead and Envelope Design for Investment Company

We need a letterhead and envelope design.
We are a family owned investment company doing direct investments into other family owned businesses.
I have attached all our current marketing material including our logo for reference.

Our under construction website can be found here:
https://rob-darke-qv7m.pagevorlo.com/
password: Copperfen

Target Market(s)

Bankers, business owners, financial partners

Industry/Entity Type

Investment

Colors

Designer to choose colors to be used in the design.

Requirements
Must have
• Logo, and company information

```html
<!DOCTYPE html>
<html lang="en">
<head>
<meta charset="utf-8">
<title>Copperfen Holdings Inc — Stationery</title>
<link rel="stylesheet" href="https://fonts.googleapis.com/css2?family=Cinzel:wght@500&family=Raleway:wght@400;500&display=swap">
<style>
  :root{
    --backdrop:#bdbdbd;
    --paper:#ffffff;
    --paper-shade:#f3f3f3;
    --gold:#d9bb63;
    --gold-deep:#c9a646;
    --ink:#2b2b2b;
    --ink-soft:#3d3d3d;
  }
  *{margin:0;padding:0;box-sizing:border-box}
  html,body{width:1200px;height:1001px;overflow:hidden}
  body{background:var(--backdrop);font-family:"Raleway",sans-serif;color:var(--ink);position:relative}

  .letterhead{position:absolute;left:83px;top:180px;width:497px;height:704px;background:var(--paper);box-shadow:0 2px 6px rgba(0,0,0,.18)}
  .letterhead__band{position:absolute;left:0;top:0;width:23px;height:100%;background:var(--gold)}

  .wordmark{position:absolute;display:flex;align-items:center;gap:8px;font-family:"Cinzel",serif;font-weight:500;color:var(--ink-soft);white-space:nowrap}
  .wordmark__mark{width:9px;height:9px;background:var(--gold)}
  .wordmark__name{display:flex;flex-direction:column;align-items:center;line-height:1.1}
  .wordmark__inc{font-size:.6em}

  .letterhead .wordmark{left:222px;top:78px;font-size:19px}

  .letter-body{position:absolute;left:227px;top:193px;width:227px;font-size:7px;line-height:12.3px;color:var(--ink-soft);text-align:justify}
  .letter-body p+p{margin-top:18px}

  .letter-footer{position:absolute;left:164px;top:649px;font-size:7.3px;line-height:14px;color:var(--ink-soft);white-space:nowrap}
  .letter-footer .sep{color:var(--gold-deep);margin:0 5px}

  .envelope{position:absolute;background:var(--paper);box-shadow:0 2px 6px rgba(0,0,0,.18);overflow:hidden}
  .envelope--front{left:622px;top:185px;width:496px;height:248px}
  .envelope--front .wordmark{left:166px;top:90px;font-size:16px}
  .envelope__web{position:absolute;left:0;width:100%;top:168px;text-align:center;font-family:"Cinzel",serif;font-size:7px;font-weight:500;color:var(--ink)}

  .envelope--back{left:620px;top:466px;width:496px;height:248px;background:linear-gradient(180deg,var(--paper) 0%,var(--paper-shade) 100%)}
  .envelope__flap{position:absolute;left:0;top:0;width:100%;height:84px}
</style>
</head>
<body>
  <section class="letterhead" aria-label="Letterhead">
    <div class="letterhead__band"></div>
    <div class="wordmark">
      <span class="wordmark__mark"></span>
      <span class="wordmark__name">COPPERFEN HOLDINGS<span class="wordmark__inc">INC</span></span>
    </div>
    <div class="letter-body">
      <p>Lorem ipsum dolor sit amet, consectetuer adipiscing elit. Aenean commodo ligula eget dolor. Aenean massa. Cum sociis natoque penatibus et magnis dis parturient montes, nascetur ridiculus mus. Donec quam felis, ultricies nec, pellentesque eu, pretium quis, sem. Nulla consequat massa quis enim. Donec pede justo, fringilla vel, aliquet nec, vulputate eget, arcu. In enim justo, rhoncus ut, imperdiet a, venenatis vitae, justo. Nullam dictum felis eu pede mollis pretium. Integer tincidunt.</p>
      <p>Cras dapibus. Vivamus elementum semper nisi. Aenean vulputate eleifend tellus. Aenean leo ligula, porttitor eu, consequat vitae, eleifend ac, enim. Aliquam lorem ante, dapibus in, viverra quis, feugiat a, tellus. Phasellus viverra nulla ut metus varius laoreet. Quisque rutrum. Aenean imperdiet. Etiam ultricies nisi vel augue. Curabitur ullamcorper ultricies nisi. Nam eget dui. Etiam rhoncus. Maecenas tempus, tellus eget condimentum rhoncus, sem quam semper libero, sit amet adipiscing sem neque sed ipsum. Nam quam nunc, blandit vel, luctus pulvinar, hendrerit id, lorem. Maecenas nec odio et ante tincidunt tempus. Donec vitae sapien ut libero venenatis faucibus. Nullam quis ante. Etiam sit amet orci eget eros faucibus tincidunt. Duis leo. Sed fringilla mauris sit amet nibh. Donec sodales sagittis magna. Sed consequat, leo eget bibendum sodales, augue velit cursus nunc.</p>
    </div>
    <div class="letter-footer">
      <div>Copperfen Holdings, Inc.<span class="sep">|</span>48 Alder Row; Suite 210<span class="sep">|</span>Marlow Falls, IA 50999</div>
      <div>P: 555-014-2290<span class="sep">|</span>www.copperfenholdings.com<span class="sep">|</span>inquiries@copperfenholdings.com</div>
    </div>
  </section>

  <section class="envelope envelope--front" aria-label="Envelope front">
    <div class="wordmark">
      <span class="wordmark__mark"></span>
      <span class="wordmark__name">COPPERFEN HOLDINGS<span class="wordmark__inc">INC</span></span>
    </div>
    <div class="envelope__web">WWW.COPPERFENHOLDINGS.COM</div>
  </section>

  <section class="envelope envelope--back" aria-label="Envelope back">
    <svg class="envelope__flap" viewBox="0 0 496 84" preserveAspectRatio="none" aria-hidden="true">
      <path d="M0 0 H496 V8 L468 78 Q466 82 460 82 H36 Q30 82 28 78 L0 8 Z" fill="var(--gold)"/>
    </svg>
  </section>
</body>
</html>
```